Stonefield Partners Business Card Design

We are looking for a new business card design, we are not happy with our current design. We are a boutique management consulting firm and our clients are typically fortune 500 companies.

I have attached the current front and back that we have as well as a version of our logo that can be used. I am trying to get a higher resolution version of the logo file to upload to the project.

Target Market(s)

Fortune 500 companies are our primary client base. Financial services, life sciences, pharmaceuticals and telecom companies are

Industry/Entity Type

Management Consulting

Contact Information for Business Card

We are trying to communicate a high degree of professionalism, a somewhat minimalist perhaps with some air of whimsy (without overdoing it). Attached is the current design, front and back as well as logos. I like the current back of the card and assume we will keep the phrase the same.

From a color palette perspective, I prefer to stay with a gray scale as they are today.

Font styles to use
Sans Serif

Colors
1b1b1b
474747
ffffff

Requirements
Must have
• Two sided business card design. File format should be something that can be used outside of Photoshop like MS Publisher so that they can be edited with personal information.
• Font should be calibri or something very similar and should be available within MS Office
Should not have
• No other logos or graphics outside of the logo provided.

```html
<!DOCTYPE html>
<html lang="en">
<head>
<meta charset="utf-8">
<title>Stonefield Partners Business Card</title>
<link rel="stylesheet" href="https://fonts.googleapis.com/css2?family=Montserrat:wght@300;400;600;700&family=Open+Sans:wght@400;600&display=swap">
<style>
  :root {
    --ink: #1b1b1b;
    --graphite: #474747;
    --paper: #ffffff;
    --stage: #d9d9d9;
    --muted: #cfcfcf;
  }
  * { box-sizing: border-box; margin: 0; padding: 0; }
  html, body { width: 1200px; height: 900px; overflow: hidden; }
  body {
    background: var(--stage);
    display: flex;
    flex-direction: column;
    align-items: center;
    justify-content: center;
    gap: 50px;
    font-family: "Open Sans", sans-serif;
  }
  .card {
    position: relative;
    width: 630px;
    height: 360px;
    border-radius: 22px;
    overflow: hidden;
    box-shadow: 0 10px 26px rgba(0,0,0,0.25);
  }

  /* Back side */
  .card-back { background: var(--ink); color: var(--paper); }
  .tagline {
    position: absolute;
    left: 60px;
    top: 140px;
    font-family: "Montserrat", sans-serif;
  }
  .tagline-lead {
    font-weight: 700;
    font-size: 24px;
    letter-spacing: 8px;
  }
  .tagline-sub {
    font-weight: 300;
    font-size: 23px;
    letter-spacing: 1px;
    margin-top: 4px;
  }
  .back-url {
    position: absolute;
    right: 50px;
    bottom: 40px;
    font-family: "Montserrat", sans-serif;
    font-size: 15px;
    color: var(--muted);
  }
  .back-url strong { color: var(--paper); font-weight: 600; }

  /* Front side */
  .card-front { background: var(--paper); color: var(--ink); }
  .front-band {
    position: absolute;
    left: 0; right: 0; bottom: 0;
    height: 150px;
    background: var(--ink);
  }
  .wordmark {
    position: absolute;
    left: 40px;
    top: 142px;
    display: flex;
    align-items: center;
    gap: 12px;
    font-family: "Montserrat", sans-serif;
    font-weight: 600;
    font-size: 44px;
    line-height: 1;
    color: var(--ink);
  }
  .wordmark-dot {
    width: 22px; height: 22px;
    border-radius: 50%;
    background: var(--ink);
  }
  .office {
    position: absolute;
    right: 40px;
    top: 34px;
    text-align: right;
    font-family: "Montserrat", sans-serif;
    font-size: 14px;
    line-height: 1.4;
    color: var(--graphite);
  }
  .office-name {
    font-weight: 700;
    font-size: 18px;
    color: var(--ink);
    margin-bottom: 2px;
  }
  .person {
    position: absolute;
    left: 40px;
    bottom: 20px;
    color: var(--paper);
    font-size: 13px;
    line-height: 1.5;
  }
  .person-name {
    font-family: "Montserrat", sans-serif;
    font-weight: 700;
    font-size: 20px;
    line-height: 1.2;
  }
  .person-role { color: var(--muted); }
  .contact-list { list-style: none; margin-top: 6px; }
  .contact-list li { display: flex; align-items: center; gap: 10px; }
  .contact-list svg { width: 12px; height: 12px; flex: none; }
  .contact-list strong { font-weight: 600; }
</style>
</head>
<body>

  <section class="card card-back" aria-label="Card back">
    <div class="tagline">
      <p class="tagline-lead">THE TRUSTED PARTNER</p>
      <p class="tagline-sub">FOR BOARDROOM-LEVEL DECISIONS</p>
    </div>
    <p class="back-url">www.<strong>stonefieldpartners</strong>.com</p>
  </section>

  <section class="card card-front" aria-label="Card front">
    <div class="office">
      <p class="office-name">Stonefield Partners, Inc.</p>
      <p>Headquarters</p>
      <p>218 Harbor View Road</p>
      <p>Suite 210</p>
      <p>Cedar Point, WA 98000</p>
    </div>

    <div class="wordmark">
      <span class="wordmark-dot"></span>
      <span>Stonefield</span>
    </div>

    <div class="front-band"></div>

    <div class="person">
      <p class="person-name">Mara Ellison</p>
      <p class="person-role">Los Angeles Office</p>
      <p class="person-role">Managing Director</p>
      <ul class="contact-list">
        <li>
          <svg viewBox="0 0 24 24" aria-hidden="true"><path fill="#ffffff" d="M6.6 10.8a15.1 15.1 0 0 0 6.6 6.6l2.2-2.2a1 1 0 0 1 1-.25 11.4 11.4 0 0 0 3.6.57 1 1 0 0 1 1 1V20a1 1 0 0 1-1 1A17 17 0 0 1 3 4a1 1 0 0 1 1-1h3.5a1 1 0 0 1 1 1c0 1.25.2 2.45.57 3.6a1 1 0 0 1-.25 1z"/></svg>
          <span>206.555.0142</span>
        </li>
        <li>
          <svg viewBox="0 0 24 24" aria-hidden="true"><rect x="2" y="5" width="20" height="14" rx="2" fill="none" stroke="#ffffff" stroke-width="2"/><path d="M3 6l9 7 9-7" fill="none" stroke="#ffffff" stroke-width="2"/></svg>
          <span>mellison@stonefieldpartners.com</span>
        </li>
        <li>
          <svg viewBox="0 0 24 24" aria-hidden="true"><circle cx="12" cy="12" r="10" fill="none" stroke="#ffffff" stroke-width="2"/><path d="M2 12h20M12 2c3 3 3 17 0 20M12 2c-3 3-3 17 0 20" fill="none" stroke="#ffffff" stroke-width="1.6"/></svg>
          <span>www.<strong>stonefieldpartners</strong>.com</span>
        </li>
      </ul>
    </div>
  </section>

</body>
</html>
```